Company brochure for our unique consulting business

We are a small consulting business offering a unique set of services to our clients.. In simple terms we are a business improvement consultancy helping our clients get the best out of their businesses. We work with clients across multiple sectors and deliver a variety of services. We want to put together a brochure to cover these main themes:1. Who we are2. What we do3. The type of people we employ4. The sectors we work inWhile the brochure needs to have a certain corporate feel to it, we don't want it to be "boring" or "stiff". We would like it to have a slightly "friendly" or "informal" feel to it, to reflect the type of organisation we are.We have a company website http://halvorkeyadvisory.example , however we do not want to directly replicate the content or feel as we recognise it needs updating.We would like the brochure to be A4 portrait format. We anticipate requiring 12 sides (including covers) but we are happy to be guided on this based on the content we have provided.The attached ppt file gives the detail of the content to be included and also shows the proposed pagination. For the front cover we would like to try 2 versions, one with the HKA logo and one with the Halvor Key Advisory logo (a file of both is attached)One of the most important pages will be the "Our Services" page. We would like this to cover the centre fold. In the ppt file we have shown an example layout, but this is where we need most help - we are clearly not graphic designers! This page will be the most used page in sales meetings etc.Also attached is the following:1. file for our HalvorKey Advisory company logo.2. File for our HKA company logo3. Files for Oren's signatures (for under photos) - Duncan's to follow4. Photo of Oren & Duncan (person in purple shirt to be cropped out)Thank you and really excited to see what everyone comes back with.Oren & Duncan

Target Market(s)

Very broad - Manufacturing, Healthcare, Hospitality

Industry/Entity Type

Management Consulting

Font styles to use
Other font styles liked:
• We use Swiss721, but happy to be guided by designer

Colors
3276b5
85abd2
0355a3
333333
5c5c5c
9d9d9d
d9d9d9

Requirements
Must have
• Corporate feel
Nice to have
• Slightly friendly feel
• Our standard "blue" is (CORRECTION) - R55 G96 B146 #376092 and our standard grey is R197 G178, B179 - #B3B2B2, which we would like to keep, but other colours we are happy to be guided on. Brand guidelines attached.

```html
<!DOCTYPE html>
<html lang="en">
<head>
<meta charset="utf-8">
<title>Halvor Key Advisory — Company Brochure</title>
<link rel="stylesheet" href="https://fonts.googleapis.com/css2?family=Open+Sans:wght@400;600;700&family=Oswald:wght@400;500&display=swap">
<style>
  :root{
    --canvas:#e6e7e9;
    --paper:#ffffff;
    --blue:#3276b5;
    --blue-deep:#0355a3;
    --blue-brand:#376092;
    --blue-light:#85abd2;
    --ink:#333333;
    --ink-soft:#5c5c5c;
    --grey:#9d9d9d;
    --grey-light:#d9d9d9;
    --night:#121314;
  }
  *{box-sizing:border-box;margin:0;padding:0}
  html,body{width:1200px;height:2270px;overflow:hidden}
  body{background:var(--canvas);font-family:"Open Sans",Arial,sans-serif;color:var(--ink);position:relative}

  .page{position:absolute;width:460px;height:650px;overflow:hidden;background:var(--paper)}
  .spread{position:absolute;width:920px;height:650px;left:140px}
  .spread .page:first-child{left:0;top:0}
  .spread .page:last-child{left:460px;top:0}
  .cover-solo{left:370px;top:50px}
  .spread-covers{top:790px}
  .spread-inside{top:1550px}
  .shapes{position:absolute;inset:0;width:100%;height:100%}

  /* ---------- Front cover ---------- */
  .wordmark{position:absolute;left:0;right:0;top:34px;display:flex;justify-content:center;align-items:center;gap:10px;
    font-weight:700;font-size:26px;color:var(--ink);letter-spacing:-.3px}
  .wordmark .mark-square{width:14px;height:14px;background:var(--blue-deep)}
  .cover-photo{position:absolute;left:0;top:92px;width:460px;height:440px;
    background:linear-gradient(170deg,#9aa0a7 0%,#dfe2e6 35%,#b7bcc2 60%,#5e6369 100%)}
  .cover-headline{position:absolute;left:92px;top:404px;font-family:"Oswald",Arial,sans-serif;font-weight:400;
    font-size:27px;line-height:1.18;color:#fff;letter-spacing:.5px}
  .cover-foot{position:absolute;left:0;top:520px;width:460px;height:130px;
    background:linear-gradient(180deg,#3b3c3e 0%,#161718 55%,#0b0b0c 100%)}
  .cover-tagline{position:absolute;left:40px;top:548px;font-size:15px;color:var(--blue-light);font-weight:600}
  .cover-url{position:absolute;right:36px;top:594px;font-size:14px;font-weight:700;color:#fff}

  /* ---------- Back cover ---------- */
  .back-photo-tower{position:absolute;left:0;top:0;width:210px;height:112px;
    background:linear-gradient(135deg,#f4f5f6 0%,#c9ccd0 50%,#8d9197 100%)}
  .back-photo-meeting{position:absolute;left:190px;top:12px;width:250px;height:104px;
    background:linear-gradient(100deg,#e9eaec 0%,#a9adb2 45%,#6f747a 100%);border-bottom:5px solid var(--blue)}
  .section-title{font-weight:700;color:var(--blue-deep);text-transform:uppercase;letter-spacing:.5px}
  .back-quotes-title{position:absolute;left:30px;top:128px;font-size:17px}
  .quote-list{position:absolute;left:30px;top:156px;width:400px;list-style:none}
  .quote-list li{font-size:10.5px;line-height:1.5;color:var(--ink-soft);margin-bottom:9px}
  .quote-list cite{font-style:normal;font-weight:700;color:var(--blue)}
  .contact-panel{position:absolute;left:0;top:350px;width:460px;height:215px;
    background:linear-gradient(160deg,var(--blue) 0%,var(--blue-brand) 60%,var(--blue-deep) 100%)}
  .contact-map{position:absolute;left:170px;top:70px;width:280px;height:130px;border-radius:6px;
    background:radial-gradient(ellipse at 50% 50%,rgba(133,171,210,.55) 0%,rgba(133,171,210,0) 70%)}
  .contact-title{position:absolute;left:28px;top:22px;font-size:16px;font-weight:700;color:#fff;letter-spacing:.5px}
  .contact-logo{position:absolute;left:250px;top:12px;font-size:30px;font-weight:700;color:#fff;display:flex;align-items:center;gap:8px}
  .contact-logo .mark-square{width:12px;height:12px;background:#fff}
  .contact-intro{position:absolute;left:28px;top:56px;width:230px;font-size:10px;line-height:1.5;color:#e6eef7}
  .contact-list{position:absolute;left:28px;top:104px;list-style:none}
  .contact-list li{display:flex;align-items:center;gap:8px;font-size:10.5px;color:#fff;margin-bottom:6px}
  .contact-list li.company{font-weight:700;font-size:11.5px}
  .contact-list svg{width:12px;height:12px;flex:none}
  .back-foot{position:absolute;left:0;top:565px;width:460px;height:85px;background:linear-gradient(180deg,#2f3032,#0b0b0c)}

  /* ---------- Inside left: about ---------- */
  .about-photo{position:absolute;left:0;top:0;width:460px;height:200px;
    background:linear-gradient(180deg,#f2f3f4 0%,#c3c6ca 45%,#6a6e73 100%)}
  .about-band{position:absolute;left:0;top:200px;width:460px;height:72px;
    background:linear-gradient(90deg,var(--blue-deep),var(--blue))}
  .about-band-text{position:absolute;left:200px;top:10px;width:240px;font-size:9.5px;line-height:1.45;color:#e6eef7}
  .about-title{position:absolute;left:28px;top:40px;font-size:18px;font-weight:700;color:#fff;letter-spacing:.5px}
  .about-intro{position:absolute;left:28px;top:292px;width:175px;font-size:10.5px;line-height:1.55;color:var(--ink-soft)}
  .partner{position:absolute;left:28px;display:flex;align-items:center;gap:12px}
  .partner-one{top:440px}
  .partner-two{top:520px}
  .partner-photo{width:48px;height:48px;border-radius:50%;background:linear-gradient(160deg,#d4d6d9,#8c9095)}
  .partner-name{font-size:11px;font-weight:700;color:var(--ink)}
  .partner-role{font-size:9.5px;color:var(--grey)}
  .partner-signature{width:60px;height:14px;margin-top:3px;background:linear-gradient(90deg,rgba(51,51,51,.35),rgba(51,51,51,0))}
  .values-title{position:absolute;left:228px;top:290px;font-size:17px;color:var(--ink)}
  .values-list{position:absolute;left:228px;top:320px;width:210px;list-style:none}
  .values-list li{display:flex;gap:8px;font-size:9.8px;line-height:1.5;color:var(--ink-soft);margin-bottom:10px}
  .values-list svg{width:11px;height:11px;flex:none;margin-top:2px}
  .values-list strong{color:var(--blue);font-weight:700}
  .inside-foot{position:absolute;left:0;top:624px;width:460px;height:26px;background:linear-gradient(180deg,#2f3032,#0b0b0c)}

  /* ---------- Inside right: regions & people ---------- */
  .regions-map{position:absolute;left:40px;top:24px;width:390px;height:170px;border-radius:4px;
    background:radial-gradient(ellipse at 50% 50%,var(--blue) 0%,var(--blue-light) 55%,rgba(133,171,210,0) 75%)}
  .regions-band{position:absolute;left:0;top:205px;width:460px;height:52px;
    background:linear-gradient(90deg,var(--blue-deep),var(--blue))}
  .regions-title{position:absolute;left:26px;top:16px;font-size:16px;font-weight:700;color:#fff;letter-spacing:.5px}
  .regions-list{position:absolute;left:160px;top:8px;width:280px;list-style:none;display:grid;grid-template-columns:1fr 1fr;row-gap:4px}
  .regions-list li{font-size:10.5px;color:#fff;display:flex;align-items:center;gap:6px}
  .regions-list li::before{content:"";width:4px;height:4px;border-radius:50%;background:#fff}
  .people-box{position:absolute;left:28px;top:290px;width:404px;height:200px;border:1px solid var(--grey-light);padding:28px 22px 0}
  .people-title{position:absolute;left:50%;top:-10px;transform:translateX(-50%);background:var(--paper);padding:0 12px;font-size:14px;color:var(--blue)}
  .people-box p{font-size:10.3px;line-height:1.6;color:var(--ink-soft);margin-bottom:10px}
</style>
</head>
<body>

<!-- Front cover, single view -->
<section class="page cover-solo" aria-label="Front cover">
  <div class="cover-photo" role="img" aria-label="Black and white photo looking up at office towers against a cloudy sky"></div>
  <svg class="shapes" viewBox="0 0 460 650" aria-hidden="true">
    <polygon points="150,100 460,86 460,104 150,114" fill="var(--blue-deep)"/>
    <polygon points="70,398 460,356 460,470 88,494" fill="var(--blue)" opacity=".82"/>
    <polygon points="70,398 300,373 316,486 88,494" fill="var(--blue-deep)" opacity=".55"/>
    <polygon points="0,516 460,500 460,507 0,523" fill="var(--blue)"/>
  </svg>
  <div class="wordmark"><span class="mark-square"></span>Halvor Key Advisory</div>
  <h1 class="cover-headline">BETTER PEOPLE<br>BETTER BUSINESS</h1>
  <div class="cover-foot"></div>
  <svg class="shapes" viewBox="0 0 460 650" aria-hidden="true">
    <polygon points="0,516 460,500 460,507 0,523" fill="var(--blue)"/>
  </svg>
  <p class="cover-tagline">Business Improvement by halvorkeyadvisory</p>
  <p class="cover-url">www.halvorkeyadvisory.example</p>
</section>

<!-- Back and front covers, open -->
<div class="spread spread-covers">
  <section class="page" aria-label="Back cover">
    <div class="back-photo-tower" role="img" aria-label="Black and white photo of a glass office facade"></div>
    <div class="back-photo-meeting" role="img" aria-label="Black and white photo of two colleagues talking in an office"></div>
    <h2 class="section-title back-quotes-title">Quotes</h2>
    <ul class="quote-list">
      <li>“HKA brought clarity and energy to every stage of our improvement programme, and the results speak for themselves.” <cite>Operations Director</cite></li>
      <li>“A practical, friendly team who listened first and then helped us fix what really mattered.” <cite>Managing Director</cite></li>
      <li>“Our people are now more engaged, and our customers have noticed the difference.” <cite>Hotel General Manager</cite></li>
    </ul>
    <div class="contact-panel">
      <div class="contact-map" role="img" aria-label="Faint world map"></div>
      <h2 class="contact-title">CONTACT US</h2>
      <div class="contact-logo"><span class="mark-square"></span>HKA</div>
      <p class="contact-intro">Get in touch to find out how we can help your business perform at its best.</p>
      <ul class="contact-list">
        <li class="company">HKA Limited</li>
        <li><svg viewBox="0 0 12 12"><path d="M2 1h2.5l1 3-1.5 1a6 6 0 0 0 3 3l1-1.5 3 1V10a1 1 0 0 1-1 1A9 9 0 0 1 1 2a1 1 0 0 1 1-1z" fill="#fff"/></svg>+01 555 0142 880</li>
        <li><svg viewBox="0 0 12 12"><rect x="1" y="2.5" width="10" height="7" fill="none" stroke="#fff"/><path d="M1 3l5 3.5L11 3" fill="none" stroke="#fff"/></svg>info@halvorkeyadvisory.example</li>
        <li><svg viewBox="0 0 12 12"><circle cx="6" cy="6" r="4.5" fill="none" stroke="#fff"/><path d="M1.5 6h9M6 1.5c-2 2.5-2 6.5 0 9M6 1.5c2 2.5 2 6.5 0 9" fill="none" stroke="#fff" stroke-width=".8"/></svg>www.halvorkeyadvisory.example</li>
        <li><svg viewBox="0 0 12 12"><path d="M6 11S2 7 2 4.5a4 4 0 0 1 8 0C10 7 6 11 6 11z" fill="#fff"/><circle cx="6" cy="4.5" r="1.4" fill="var(--blue)"/></svg>12 Harbour Row, Northgate NG1 4XX</li>
      </ul>
    </div>
    <div class="back-foot"></div>
  </section>

  <section class="page" aria-label="Front cover">
    <div class="cover-photo" role="img" aria-label="Black and white photo looking up at office towers against a cloudy sky"></div>
    <svg class="shapes" viewBox="0 0 460 650" aria-hidden="true">
      <polygon points="150,100 460,86 460,104 150,114" fill="var(--blue-deep)"/>
      <polygon points="70,398 460,356 460,470 88,494" fill="var(--blue)" opacity=".82"/>
      <polygon points="70,398 300,373 316,486 88,494" fill="var(--blue-deep)" opacity=".55"/>
    </svg>
    <div class="wordmark"><span class="mark-square"></span>Halvor Key Advisory</div>
    <h2 class="cover-headline">BETTER PEOPLE<br>BETTER BUSINESS</h2>
    <div class="cover-foot"></div>
    <svg class="shapes" viewBox="0 0 460 650" aria-hidden="true">
      <polygon points="0,516 460,500 460,507 0,523" fill="var(--blue)"/>
    </svg>
    <p class="cover-tagline">Business Improvement by halvorkeyadvisory</p>
    <p class="cover-url">www.halvorkeyadvisory.example</p>
  </section>
</div>

<!-- Inside spread -->
<div class="spread spread-inside">
  <section class="page" aria-label="About us">
    <div class="about-photo" role="img" aria-label="Black and white photo of a team meeting around a boardroom table"></div>
    <div class="about-band">
      <p class="about-band-text">At HKA we constantly strive to deliver the best possible value for our clients, helping them improve every day.</p>
      <h2 class="about-title">ABOUT US</h2>
    </div>
    <p class="about-intro">We bring together our expertise from years of experience working with multiple organisations to help our clients deliver results against their individual goals.</p>
    <div class="partner partner-one">
      <div class="partner-photo" role="img" aria-label="Portrait photo of Duncan Reyes"></div>
      <div>
        <p class="partner-name">Duncan Reyes</p>
        <p class="partner-role">Partner</p>
        <div class="partner-signature" role="img" aria-label="Signature of Duncan Reyes"></div>
      </div>
    </div>
    <div class="partner partner-two">
      <div class="partner-photo" role="img" aria-label="Portrait photo of Oren Vale"></div>
      <div>
        <p class="partner-name">Oren Vale</p>
        <p class="partner-role">Partner</p>
        <div class="partner-signature" role="img" aria-label="Signature of Oren Vale"></div>
      </div>
    </div>
    <h2 class="section-title values-title">Our Values</h2>
    <ul class="values-list">
      <li><svg viewBox="0 0 11 11"><rect width="11" height="11" rx="2" fill="var(--blue)"/><path d="M2.5 5.5l2 2 4-4" fill="none" stroke="#fff" stroke-width="1.4"/></svg><span>Be <strong>TRUSTED</strong> by our team and clients, so that our opinions are valued.</span></li>
      <li><svg viewBox="0 0 11 11"><rect width="11" height="11" rx="2" fill="var(--blue)"/><path d="M2.5 5.5l2 2 4-4" fill="none" stroke="#fff" stroke-width="1.4"/></svg><span>Build a long-term relationship with our clients as a <strong>PARTNER</strong>, not just a supplier.</span></li>
      <li><svg viewBox="0 0 11 11"><rect width="11" height="11" rx="2" fill="var(--blue)"/><path d="M2.5 5.5l2 2 4-4" fill="none" stroke="#fff" stroke-width="1.4"/></svg><span>Be focused on return on investment, so clients always receive <strong>GREAT VALUE</strong>.</span></li>
      <li><svg viewBox="0 0 11 11"><rect width="11" height="11" rx="2" fill="var(--blue)"/><path d="M2.5 5.5l2 2 4-4" fill="none" stroke="#fff" stroke-width="1.4"/></svg><span><strong>DEVELOP</strong> and <strong>INVEST</strong> in our own people so they can perform at their best.</span></li>
      <li><svg viewBox="0 0 11 11"><rect width="11" height="11" rx="2" fill="var(--blue)"/><path d="M2.5 5.5l2 2 4-4" fill="none" stroke="#fff" stroke-width="1.4"/></svg><span>Take <strong>SOCIAL RESPONSIBILITY</strong> seriously by supporting worthwhile local organisations.</span></li>
    </ul>
    <div class="inside-foot"></div>
  </section>

  <section class="page" aria-label="Our regions and our people">
    <div class="regions-map" role="img" aria-label="World map with location pins on the regions served"></div>
    <div class="regions-band">
      <h2 class="regions-title">OUR REGIONS</h2>
      <ul class="regions-list">
        <li>North America</li>
        <li>Europe</li>
        <li>UK &amp; Ireland</li>
        <li>Middle East</li>
      </ul>
    </div>
    <div class="people-box">
      <h2 class="section-title people-title">Our People</h2>
      <p>All of our team at HKA started their careers in operational roles. This means we understand what it's like to be in your shoes, and we work alongside your people to achieve great results together.</p>
      <p>We also recognise that engagement matters. Everyone in your team will get to know us on first name terms, because we take the time to listen.</p>
    </div>
    <div class="inside-foot"></div>
  </section>
</div>

</body>
</html>
```